Hoofcare business card

I would like to create a business card design for my hoofcare business.

Front Side- would like to just include the logo and text as per the uploaded files- text font to match logo (upper and lower case).

Back side
- Include the details and contact information provided on the uploaded file.
- Also included on the back side- the uploaded TRUMV logo- keep it small on a top or bottom corner
- for facebook and Instagram contacts- please use the logos next to my usernames

```html
<!DOCTYPE html>
<html lang="en">
<head>
<meta charset="utf-8">
<title>KR Equine Hoofcare – Business Card</title>
<link href="https://fonts.googleapis.com/css2?family=Cinzel:wght@400;600&display=swap" rel="stylesheet">
<style>
  :root{
    --stage:#cfcfd1;
    --card:#1b1b1c;
    --ink:#e6e6e6;
    --silver:#c9cacc;
    --muted:#a9a9ab;
    --rule:#5a5a5c;
    --badge:#d8d8da;
  }
  *{box-sizing:border-box;margin:0;padding:0}
  html,body{width:1200px;height:800px;overflow:hidden}
  body{
    background:var(--stage);
    display:flex;align-items:center;justify-content:center;gap:40px;
    font-family:"Cinzel",serif;color:var(--ink);
  }
  .card{
    width:540px;height:308px;background:var(--card);
    position:relative;box-shadow:0 6px 18px rgba(0,0,0,.25);
  }
  /* back side */
  .brand-mark{position:absolute;left:36px;top:72px;width:150px;text-align:center}
  .brand-mark .name{font-size:40px;font-weight:400;letter-spacing:2px;line-height:1;color:var(--ink)}
  .brand-mark .sub{font-size:11px;letter-spacing:1px;margin-top:6px}
  .divider{position:absolute;left:200px;top:56px;width:1px;height:100px;background:var(--rule)}
  .credentials{position:absolute;left:218px;top:62px;width:290px}
  .credentials h2{font-size:14px;font-weight:600;letter-spacing:.5px;line-height:1.25}
  .credentials p{font-size:9.5px;color:var(--muted);line-height:1.4;margin-top:5px}
  .partner-badge{
    position:absolute;right:34px;top:172px;width:46px;height:46px;border-radius:50%;
    background:var(--badge);
  }
  .contact{position:absolute;left:36px;bottom:30px}
  .contact .person{font-size:15px;letter-spacing:1px;margin-bottom:8px}
  .contact ul{list-style:none}
  .contact li{display:flex;align-items:center;gap:8px;font-size:11px;line-height:1.6;color:var(--ink)}
  .contact svg{width:10px;height:10px;flex:none}
  .social-circle{width:9px;height:9px;border-radius:50%;background:var(--ink);flex:none}
  .social-square{width:9px;height:9px;background:var(--ink);flex:none}
  /* front side */
  .front{display:flex;flex-direction:column;align-items:center;justify-content:center}
  .front .name{font-size:86px;letter-spacing:4px;color:var(--silver);line-height:1}
  .front .sub{font-size:20px;letter-spacing:2px;color:var(--silver);margin-top:8px}
  .front .tagline{margin-top:28px;text-align:center;font-size:12px;letter-spacing:1px;color:var(--silver);line-height:1.5}
</style>
</head>
<body>
  <section class="card back" aria-label="Back of card">
    <div class="brand-mark">
      <div class="name">KR</div>
      <div class="sub">Equine Hoofcare</div>
    </div>
    <div class="divider"></div>
    <div class="credentials">
      <h2>TRUMV Trained Barefoot Trimmer</h2>
      <p>Equine barefoot trimming and rehabilitation for all horses, ponies and donkeys.</p>
    </div>
    <div class="partner-badge" role="img" aria-label="Certification badge"></div>
    <div class="contact">
      <div class="person">Maren Tolley</div>
      <ul>
        <li><svg viewBox="0 0 10 10"><rect x="2.5" y="0.5" width="5" height="9" rx="1" fill="none" stroke="currentColor"/></svg>0400555218</li>
        <li><svg viewBox="0 0 10 10"><rect x="0.5" y="2" width="9" height="6" fill="none" stroke="currentColor"/><path d="M0.5 2 5 5.5 9.5 2" fill="none" stroke="currentColor"/></svg>krequinehoofcare@example.com</li>
        <li><span class="social-square"></span>KR Equine Hoofcare</li>
        <li><span class="social-circle"></span>krequinehoofcare</li>
      </ul>
    </div>
  </section>

  <section class="card front" aria-label="Front of card">
    <div class="name">KR</div>
    <div class="sub">Equine Hoofcare</div>
    <div class="tagline">Equine barefoot trimming and rehabilitation<br>Pelican Bay and surrounds</div>
  </section>
</body>
</html>
```